Looking for a high-end business card design for a construction company

We are looking to update our business card design. We are a post-frame construction company that builds custom buildings, commercial spaces, homes, and anything else. We have multiple people working here so we would need something we can easily customize the information for the specific person. We need a name, website, cell phone, office phone as well as social icons. Our colors are black, white, and grey/silver so I would love a black background or something that is more striking than just a traditional white business card. Looking for something that is very professional with a high-end look/feel. I have attached our logos, they can be silver, white, grey, or black.
Industry/Entity Type
Construction
Contact Information for Business Card
Business logo, Name, Cell phone, Office phone, website, social Icons
Colors
Designer to choose only greyscale colors for use in the design.
Look and feel

```html
<!DOCTYPE html>
<html lang="en">
<head>
<meta charset="utf-8">
<title>Harwell Builders, Inc. — Business Card</title>
<link href="https://fonts.googleapis.com/css2?family=Archivo:wght@800&family=Arimo:wght@400;700&display=swap" rel="stylesheet">
<style>
  :root {
    --backdrop: #e6e6e4;
    --card: #262628;
    --card-deep: #1c1c1e;
    --accent-grey: #3a3a3d;
    --silver: #b8b8bc;
    --white: #f4f4f4;
    --muted: #c9c9cc;
  }
  * { box-sizing: border-box; margin: 0; padding: 0; }
  html, body {
    width: 1200px;
    height: 801px;
    overflow: hidden;
    background: var(--backdrop);
  }
  .sheet {
    width: 1200px;
    height: 801px;
    display: flex;
    align-items: center;
    justify-content: center;
    gap: 40px;
  }
  .card {
    position: relative;
    width: 540px;
    height: 309px;
    background: var(--card);
    overflow: hidden;
    box-shadow: 0 10px 24px rgba(0, 0, 0, 0.18);
  }

  /* shared wordmark */
  .wordmark {
    display: flex;
    align-items: center;
    gap: 12px;
    color: var(--white);
  }
  .wordmark__dot {
    flex: none;
    border-radius: 50%;
    background: var(--white);
  }
  .wordmark__text {
    font-family: "Archivo", "Arial Black", sans-serif;
    font-weight: 800;
    letter-spacing: 0.14em;
    line-height: 1.05;
    text-transform: uppercase;
  }
  .wordmark__line { display: block; }

  /* front side */
  .card--front .sweep {
    position: absolute;
    right: -80px;
    top: 40px;
    width: 420px;
    height: 300px;
  }
  .card--front .wordmark {
    position: absolute;
    left: 34px;
    top: 34px;
  }
  .card--front .wordmark__dot { width: 30px; height: 30px; }
  .card--front .wordmark__line--main { font-size: 22px; }
  .card--front .wordmark__line--sub { font-size: 11px; letter-spacing: 0.2em; }

  .address {
    position: absolute;
    right: 30px;
    top: 40px;
    text-align: right;
    font-family: "Arimo", Arial, sans-serif;
    font-size: 13px;
    line-height: 1.45;
    color: var(--muted);
  }

  .person {
    position: absolute;
    left: 34px;
    bottom: 30px;
    font-family: "Arimo", Arial, sans-serif;
    color: var(--white);
  }
  .person__name {
    font-size: 18px;
    font-weight: 400;
    letter-spacing: 0.04em;
    text-transform: uppercase;
  }
  .person__role {
    font-size: 13px;
    color: var(--muted);
    margin-bottom: 16px;
  }
  .contact-list { list-style: none; }
  .contact-list__item {
    display: flex;
    align-items: center;
    gap: 10px;
    font-size: 14px;
    line-height: 1.6;
    color: var(--white);
  }
  .contact-list__icon {
    width: 13px;
    height: 13px;
    flex: none;
    fill: var(--muted);
  }

  /* back side */
  .card--back { background: linear-gradient(180deg, var(--card) 0%, var(--card-deep) 100%); }
  .card--back .sweep {
    position: absolute;
    left: 40px;
    top: 18px;
    width: 460px;
    height: 190px;
  }
  .card--back .band {
    position: absolute;
    left: 0;
    right: 0;
    bottom: 0;
    height: 96px;
    background: var(--card);
    border-top: 1px solid var(--accent-grey);
  }
  .card--back .wordmark {
    position: absolute;
    left: 50%;
    bottom: 26px;
    transform: translateX(-50%);
  }
  .card--back .wordmark__dot { width: 36px; height: 36px; }
  .card--back .wordmark__line--main { font-size: 34px; }
  .card--back .wordmark__line--sub { font-size: 17px; letter-spacing: 0.2em; }
</style>
</head>
<body>
<main class="sheet">

  <section class="card card--front" aria-label="Business card front">
    <svg class="sweep" viewBox="0 0 420 300" aria-hidden="true">
      <ellipse cx="210" cy="150" rx="200" ry="90" transform="rotate(-18 210 150)" fill="#2e2e31"/>
    </svg>

    <div class="wordmark">
      <span class="wordmark__dot"></span>
      <span class="wordmark__text">
        <span class="wordmark__line wordmark__line--main">Harwell</span>
        <span class="wordmark__line wordmark__line--sub">Builders, Inc.</span>
      </span>
    </div>

    <address class="address">
      Your address<br>
      city, state, ZIP 0000
    </address>

    <div class="person">
      <h1 class="person__name">Jonathan Smith</h1>
      <p class="person__role">Manager</p>
      <ul class="contact-list">
        <li class="contact-list__item">
          <svg class="contact-list__icon" viewBox="0 0 24 24" aria-hidden="true"><path d="M6.6 10.8a15.1 15.1 0 0 0 6.6 6.6l2.2-2.2a1 1 0 0 1 1-.25 11.4 11.4 0 0 0 3.6.57 1 1 0 0 1 1 1V20a1 1 0 0 1-1 1A17 17 0 0 1 3 4a1 1 0 0 1 1-1h3.5a1 1 0 0 1 1 1c0 1.25.2 2.45.57 3.6a1 1 0 0 1-.25 1z"/></svg>
          123-456-2100
        </li>
        <li class="contact-list__item">
          <svg class="contact-list__icon" viewBox="0 0 24 24" aria-hidden="true"><path d="M2 5h20v14H2zm2 2v.5l8 5 8-5V7zm0 2.9V17h16V9.9l-8 5z"/></svg>
          youremail@mailbox.com
        </li>
        <li class="contact-list__item">
          <svg class="contact-list__icon" viewBox="0 0 24 24" aria-hidden="true"><path d="M12 2a10 10 0 1 0 0 20 10 10 0 0 0 0-20zm6.9 6h-3a15 15 0 0 0-1.3-3.9A8 8 0 0 1 18.9 8zM12 4a13 13 0 0 1 1.9 4h-3.8A13 13 0 0 1 12 4zM4.3 14a8 8 0 0 1 0-4h3.4a16 16 0 0 0 0 4zm.8 2h3a15 15 0 0 0 1.3 3.9A8 8 0 0 1 5.1 16zm3-8h-3a8 8 0 0 1 4.3-3.9A15 15 0 0 0 8.1 8zM12 20a13 13 0 0 1-1.9-4h3.8A13 13 0 0 1 12 20zm2.3-6H9.7a14 14 0 0 1 0-4h4.6a14 14 0 0 1 0 4zm.3 5.9a15 15 0 0 0 1.3-3.9h3a8 8 0 0 1-4.3 3.9zm1.7-5.9a16 16 0 0 0 0-4h3.4a8 8 0 0 1 0 4z"/></svg>
          www.yourwebsite.com
        </li>
      </ul>
    </div>
  </section>

  <section class="card card--back" aria-label="Business card back">
    <svg class="sweep" viewBox="0 0 460 190" aria-hidden="true">
      <defs>
        <linearGradient id="sweep-fade" x1="0" y1="0" x2="1" y2="0">
          <stop offset="0" stop-color="#2a2a2c"/>
          <stop offset="1" stop-color="#5a5a5e"/>
        </linearGradient>
      </defs>
      <ellipse cx="230" cy="100" rx="225" ry="70" transform="rotate(-10 230 100)" fill="url(#sweep-fade)" opacity="0.6"/>
    </svg>
    <div class="band"></div>
    <div class="wordmark">
      <span class="wordmark__dot"></span>
      <span class="wordmark__text">
        <span class="wordmark__line wordmark__line--main">Harwell</span>
        <span class="wordmark__line wordmark__line--sub">Builders, Inc.</span>
      </span>
    </div>
  </section>

</main>
</body>
</html>
```